Professional banners for an eyewear company

I have 3 images which need to be made into banners. Size 990 x 370, with a 10 pixel white border at top and bottom of banner.

They all need to be adjusted to make the colours better and less bright.
All will need some writing written on them with a nice serif font.

Banner 1 text: Handcrafted luxury eyewear, with a purpose...
Banner 2 text: Half of our profits go to help malnourished children in India
Banner 3 text: 10% of your first order, use code: First Order

On our homepage these 3 banners will alternate, so they need to look good together.

Tips
Please take a look at the banners on the lunvoreck.com homepage, this is kind of how I want the text to be displayed, and they use good colours.

The backgrounds on Banners 2 & 3 can be changed.
Banner 3 background if you can change to a nice colour, as per lunvoreck.com homepage.
Updates

Hi, just a quick update, thank you for all the designs submitted so far, please keep in mind that the brand is a luxury high-end brand so designs will need to reflect this.

Industry/Entity Type

Eyewear

```html
<!DOCTYPE html>
<html lang="en">
<head>
<meta charset="utf-8">
<title>First Order Offer Banner</title>
<link href="https://fonts.googleapis.com/css2?family=Archivo+Black&family=Arimo:wght@400;700&display=swap" rel="stylesheet">
<style>
  :root {
    --paper: #ffffff;
    --teal: #5bc5cf;
    --teal-pale: #84d0d7;
    --teal-mist: #94d5dc;
    --teal-mid: #76c8ce;
    --teal-deep: #63bec5;
    --pill-top: #72d0dc;
    --pill-bottom: #3fb1c2;
    --ink-shadow: #1d3c42;
    --text: #ffffff;
    --blouse: rgba(244, 240, 236, 0.95);
    --hair: rgba(186, 112, 76, 0.75);
  }
  * { margin: 0; padding: 0; box-sizing: border-box; }
  html, body { width: 1200px; height: 448px; overflow: hidden; background: var(--paper); }
  .banner {
    position: relative;
    width: 1200px;
    height: 448px;
    background: var(--paper);
  }
  .banner__field {
    position: absolute;
    top: 12px;
    left: 0;
    width: 1200px;
    height: 424px;
    background: var(--teal);
    overflow: hidden;
  }
  .banner__photo {
    position: absolute;
    top: 0;
    left: 0;
    width: 534px;
    height: 100%;
    background:
      radial-gradient(ellipse 150px 110px at 190px 70px, var(--hair) 0%, rgba(186, 112, 76, 0) 100%),
      radial-gradient(ellipse 190px 260px at 185px 330px, var(--blouse) 0%, rgba(244, 240, 236, 0.7) 60%, rgba(244, 240, 236, 0) 100%),
      linear-gradient(90deg,
        var(--teal-pale) 0, var(--teal-pale) 400px,
        var(--teal-mist) 400px, var(--teal-mist) 430px,
        var(--teal-mid) 430px, var(--teal-mid) 497px,
        var(--teal-deep) 497px, var(--teal-deep) 534px);
  }
  .offer {
    position: absolute;
    left: 618px;
    width: 500px;
    top: 0;
    text-align: center;
    color: var(--text);
  }
  .offer__headline {
    position: absolute;
    top: 70px;
    left: 0;
    width: 100%;
    font-family: "Archivo Black", "Arial Black", sans-serif;
    white-space: nowrap;
    text-shadow: 3px 3px 0 var(--ink-shadow);
    line-height: 1;
  }
  .offer__percent { font-size: 110px; letter-spacing: -3px; }
  .offer__off { font-size: 76px; margin-left: 10px; }
  .offer__subline {
    position: absolute;
    top: 192px;
    left: 0;
    width: 100%;
    font-family: "Arimo", Arial, sans-serif;
    font-weight: 400;
    font-size: 54px;
    letter-spacing: 4px;
    line-height: 1;
    white-space: nowrap;
    text-shadow: 2px 2px 0 var(--ink-shadow);
  }
  .offer__code {
    position: absolute;
    top: 276px;
    left: 0;
    width: 500px;
    height: 73px;
    border-radius: 37px;
    background: linear-gradient(180deg, var(--pill-top) 0%, var(--pill-bottom) 100%);
    box-shadow: 0 4px 6px rgba(20, 80, 90, 0.35);
    display: flex;
    align-items: center;
    justify-content: center;
    font-family: "Arimo", Arial, sans-serif;
    font-weight: 700;
    font-size: 27px;
    text-shadow: 1px 1px 1px rgba(20, 60, 66, 0.6);
  }
</style>
</head>
<body>
  <div class="banner">
    <div class="banner__field">
      <div class="banner__photo" role="img" aria-label="Photograph of a red-haired woman in sunglasses and a polka-dot blouse, hand in her hair, looking surprised"></div>
      <div class="offer">
        <p class="offer__headline"><span class="offer__percent">10%</span><span class="offer__off">OFF</span></p>
        <p class="offer__subline">your first order</p>
        <p class="offer__code">USE CODE : FIRST ORDER</p>
      </div>
    </div>
  </div>
</body>
</html>
```